Criação de Kit Layout de Posts para Redes Sociais (Facebook, Instagram e etc) para Outros
" Empresa especializada em assessoria e consultoria em assuntos regulatórios nos órgãos sanitários para o licenciamento de cosméticos, produtos de higiene pessoal, perfumaria, medicamentos, produtos saneantes, equipamentos e produtos odontológicos, médicos e hospitalares. "

```html
<!DOCTYPE html>
<html lang="pt-BR">
<head>
<meta charset="UTF-8">
<title>Nora Assessoria – Post</title>
<link href="https://fonts.googleapis.com/css2?family=Arimo:wght@400;500&display=swap" rel="stylesheet">
<style>
  :root {
    --navy: #25397a;
    --navy-deep: #1d2f66;
    --teal: #2aa6a8;
    --white: #ffffff;
    --ink: #222a3a;
    --wood-dark: #5a3a24;
    --wood-mid: #8a5f3e;
    --wood-light: #b58a62;
  }
  * { margin: 0; padding: 0; box-sizing: border-box; }
  html, body { width: 1200px; height: 1200px; overflow: hidden; background: var(--white); }
  .post {
    position: relative;
    width: 1200px;
    height: 1200px;
    overflow: hidden;
    font-family: "Arimo", Arial, sans-serif;
    background: var(--white);
  }
  .post__photo {
    position: absolute;
    inset: 0 0 260px 0;
    background:
      radial-gradient(ellipse at 60% 45%, rgba(240,240,240,0.35), transparent 55%),
      linear-gradient(135deg, var(--wood-mid) 0%, var(--wood-dark) 45%, var(--wood-light) 75%, var(--wood-mid) 100%);
  }
  .post__headline {
    position: absolute;
    left: 96px;
    top: 64px;
    color: var(--navy);
    font-size: 100px;
    font-weight: 400;
    line-height: 1.08;
    letter-spacing: 1px;
  }
  .post__wave {
    position: absolute;
    inset: 0;
    width: 1200px;
    height: 1200px;
  }
  .contact {
    position: absolute;
    left: 62px;
    top: 1038px;
    color: var(--ink);
  }
  .contact__phone {
    display: flex;
    align-items: center;
    gap: 16px;
    font-size: 27px;
  }
  .contact__phone svg { width: 34px; height: 34px; }
  .contact__site {
    margin-top: 22px;
    font-size: 29px;
  }
  .brand {
    position: absolute;
    left: 612px;
    top: 985px;
    width: 520px;
  }
  .brand__name {
    display: flex;
    align-items: center;
    gap: 24px;
    color: var(--navy);
    font-size: 66px;
    font-weight: 500;
    letter-spacing: 1px;
    height: 110px;
  }
  .brand__mark {
    width: 70px;
    height: 70px;
    background: var(--navy);
    flex: none;
  }
  .brand__rule {
    margin-top: 18px;
    height: 2px;
    background: var(--teal);
  }
  .brand__tagline {
    margin-top: 12px;
    color: var(--teal);
    font-size: 27px;
    letter-spacing: 0.5px;
    text-align: center;
  }
</style>
</head>
<body>
<div class="post">
  <div class="post__photo" role="img" aria-label="Foto vista de cima de uma mesa de madeira com notebook, tablet, pranchetas e documentos, com duas pessoas apertando as mãos sobre a mesa"></div>

  <h1 class="post__headline">SEU<br>TEXTO<br>AQUI</h1>

  <svg class="post__wave" viewBox="0 0 1200 1200" aria-hidden="true">
    <defs>
      <linearGradient id="bandGradient" x1="0" y1="0" x2="1" y2="0">
        <stop offset="0" stop-color="#1d2f66"/>
        <stop offset="0.55" stop-color="#24508a"/>
        <stop offset="1" stop-color="#2aa6a8"/>
      </linearGradient>
    </defs>
    <path d="M0,900 C350,880 780,800 1200,790 L1200,1200 L0,1200 Z" fill="url(#bandGradient)"/>
    <path d="M0,935 C380,910 800,850 1200,860 L1200,1200 L0,1200 Z" fill="#ffffff"/>
  </svg>

  <div class="contact">
    <p class="contact__phone">
      <svg viewBox="0 0 24 24" aria-hidden="true">
        <path d="M6.6 10.8a15.1 15.1 0 0 0 6.6 6.6l2.2-2.2a1 1 0 0 1 1-.25 11.4 11.4 0 0 0 3.6.57 1 1 0 0 1 1 1V20a1 1 0 0 1-1 1A17 17 0 0 1 3 4a1 1 0 0 1 1-1h3.5a1 1 0 0 1 1 1c0 1.25.2 2.45.57 3.57a1 1 0 0 1-.25 1z" fill="#222a3a"/>
      </svg>
      (11) 3000-4821 / 9 9000-6137
    </p>
    <p class="contact__site">www.noraassessoria.com.br</p>
  </div>

  <div class="brand">
    <div class="brand__name"><span class="brand__mark"></span>Nora Assessoria</div>
    <div class="brand__rule"></div>
    <p class="brand__tagline">especializada em Vigilância Sanitária</p>
  </div>
</div>
</body>
</html>
```